Business Card (double-sided) and Stationary Design for dental office

1) Business Card Design: We need a business card design for a dental specialty office.
Texts should contain:
The name of our office "Maplecrest Family Orthodontics"
Tagline: "Specialist in Orthodontic and Maxillofacial Orthopedics"
Tag line: "Creating "Dorvaling" smiles for Children and Adults"
Doctor name: "Doctor Name"
Office Address:
"123 Street Name
City, State Zip code"
Office email address: office@maplecrestfamily.com
Website: www.maplecrestfamily.com

We will provide the full office address once the design is selected
Theme: beach, paradise, coastal, wave
We would like to have some creativity in design. Some acceptable ideas: front page: logo and office name. Back page: more detail information, and map to office in form of an island. Please see sample from our other location, but you DON'T HAVE TO USE OR COPY THE SAME CONCEPT.

IF POSSIBLE, PLEASE SUBMIT AT LEAST TWO CONCEPTS: ONE WITH THE BACK LOOKING SIMILAR TO WHAT IS IN THE SAMPLE, AND ONE DIFFERENT.

Color: designer to choose. We have different shade of blues and sand color in our office. Please see logo.

2) Please also design a matching set of stationary that compliment the business card and our logo.

Target Market(s)

Dental

Contact Information for Business Card

See descriptions

Font styles to use
Other font styles liked:
• Matching texts in logo

Colors
0054AA
0677BA
7BADD7
CADEEF
E8F1F8
0094D4
00A9DD
6FCCEA
C7EBF8
E9F6FB
00AB8E
00BBA5
67D7C9
C6EFE9
E9F9F6

Requirements
Must have
• Double-sided
Nice to have
• Beach coastal theme
Should not have
• Any shape or drawing of of tooth or teeth. We don’t need these. You don't necessarily have to just cut and paste the logo art and text as a whole, you have the liberty to rearrange the text.

```html
<!DOCTYPE html>
<html lang="en">
<head>
<meta charset="utf-8">
<title>Maplecrest Family Orthodontics – Business Card</title>
<link rel="stylesheet" href="https://fonts.googleapis.com/css2?family=Roboto:wght@300;400;500&display=swap">
<style>
  :root {
    --teal: #3a8fa8;
    --mint: #80cbbb;
    --ink: #262626;
    --ink-soft: #3a3a3a;
    --paper: #ffffff;
    --backdrop: #e6e8ec;
    --map-tint: #f3f4f5;
  }
  html, body {
    margin: 0;
    width: 1200px;
    height: 1200px;
    overflow: hidden;
    background: var(--backdrop);
    font-family: "Roboto", sans-serif;
  }
  .card {
    position: absolute;
    display: block;
    background: var(--paper);
    box-shadow: 0 6px 18px rgba(0,0,0,0.18);
  }
  .card--front { left: 125px; top: 28px; width: 950px; height: 555px; }
  .card--back  { left: 130px; top: 615px; width: 939px; height: 554px; }
  .fill-teal { fill: var(--teal); }
  .fill-mint { fill: var(--mint); }
  .brand-name { font: 500 30px "Roboto", sans-serif; fill: var(--teal); }
  .brand-tag { font: 400 10px "Roboto", sans-serif; fill: var(--mint); letter-spacing: 1px; }
  .web-front { font: 400 26px "Roboto", sans-serif; fill: var(--ink-soft); }
  .person-first { font: 500 38px "Roboto", sans-serif; fill: var(--ink); }
  .person-last { fill: var(--teal); }
  .person-role { font: 400 23px "Roboto", sans-serif; fill: var(--ink); }
  .contact-line { font: 300 23px "Roboto", sans-serif; fill: var(--ink-soft); }
  .band-slogan { font: 400 20px "Roboto", sans-serif; fill: #ffffff; }
  .icon-stroke { fill: none; stroke: #ffffff; stroke-width: 2.4; stroke-linecap: round; stroke-linejoin: round; }
</style>
</head>
<body>

<svg class="card card--front" viewBox="0 0 950 555" xmlns="http://www.w3.org/2000/svg">
  <rect class="world-map" x="40" y="40" width="870" height="420" rx="30" fill="var(--map-tint)" opacity="0.6" role="img" aria-label="Faint world map in the background"/>
  <circle class="brand-mark fill-teal" cx="475" cy="224" r="92"/>
  <text class="brand-name" x="475" y="357" text-anchor="middle">Maplecrest Family Orthodontics</text>
  <rect class="fill-mint" x="322" y="371" width="18" height="3"/>
  <rect class="fill-mint" x="610" y="371" width="18" height="3"/>
  <text class="brand-tag" x="475" y="376" text-anchor="middle">Pediatric Dentistry &amp; Orthodontics</text>

  <polygon class="fill-mint" points="8,510 50,474 170,474 128,510"/>
  <polygon class="fill-teal" points="139,510 181,474 300,474 258,510"/>
  <text class="web-front" x="470" y="504" text-anchor="middle">www.maplecrestfamily.com</text>
  <polygon class="fill-mint" points="635,510 675,474 798,474 756,510"/>
  <polygon class="fill-teal" points="768,510 808,474 930,474 889,510"/>
  <rect class="fill-teal" x="0" y="544" width="950" height="11"/>
</svg>

<svg class="card card--back" viewBox="0 0 939 554" xmlns="http://www.w3.org/2000/svg">
  <rect class="fill-teal" x="34" y="64" width="12" height="89"/>
  <rect class="fill-mint" x="50" y="64" width="12" height="89"/>
  <text class="person-first" x="74" y="95">CLARA <tspan class="person-last">WHITFORD</tspan></text>
  <text class="person-role" x="74" y="125">Specialist in Orthodontic</text>
  <text class="person-role" x="74" y="154">and Maxillofacial Orthopedics</text>

  <rect x="742" y="52" width="146" height="168" rx="8" fill="var(--mint)"/>
  <rect x="745" y="55" width="140" height="162" rx="6" fill="#dfe4e6" role="img" aria-label="Portrait photo of the orthodontist in a white coat"/>

  <g class="contact-phone">
    <circle class="fill-teal" cx="62" cy="325" r="26"/>
    <path class="icon-stroke" d="M53 314 l6 -2 4 8 -4 3 q3 7 10 10 l3 -4 8 4 -2 6 q-18 2 -25 -25z"/>
    <text class="contact-line" x="105" y="318">014 . 552. 3190</text>
    <text class="contact-line" x="105" y="347">014 . 552. 3190</text>
  </g>
  <g class="contact-web">
    <circle class="fill-teal" cx="62" cy="403" r="26"/>
    <circle class="icon-stroke" cx="62" cy="403" r="15"/>
    <ellipse class="icon-stroke" cx="62" cy="403" rx="6" ry="15"/>
    <path class="icon-stroke" d="M47 403 h30 M49 395 h26 M49 411 h26"/>
    <text class="contact-line" x="105" y="398">office@maplecrestfamily.com</text>
    <text class="contact-line" x="105" y="427">www.maplecrestfamily.com</text>
  </g>
  <g class="contact-address">
    <circle class="fill-teal" cx="62" cy="482" r="26"/>
    <path d="M62 500 q-13 -15 -13 -24 a13 13 0 0 1 26 0 q0 9 -13 24z" fill="#ffffff"/>
    <circle class="fill-teal" cx="62" cy="476" r="5"/>
    <text class="contact-line" x="105" y="474">418 Harborview Lane</text>
    <text class="contact-line" x="105" y="503">Seabrook, AK 99841</text>
  </g>

  <polygon class="fill-mint" points="345,505 363,477 588,477 568,505"/>
  <polygon class="fill-teal" points="574,505 614,451 939,451 939,505"/>
  <text class="band-slogan" x="758" y="486" text-anchor="middle">Smiles for Children and Adults</text>
  <rect class="fill-teal" x="0" y="538" width="939" height="16"/>
</svg>

</body>
</html>
```